ClipStream banner - Girl illustration, technology, green, blue, spring-like

I need help for clipstream art for my banner. There are strict channel art templates. I have no ideas at all but hope if you look at some of my videos you will learn a bit about me.

My channel:
https://www.clipstream.example/channel/UXQPLM93hd7t2K6Vfrwz0bQa

My channel is on Tarmix, technology, information security, and some technical demonstration videos.

Channel templates can be found here
https://help.quorvel.example/clipstream/answer/5810446?hl=en

Here is what I don't like:
- pictures of "hackers" - boys with hoodies on
- pictures of circuit boards

Can show my name "LJ Harrowby" preferred, cursive is good, or blackboard type fun font

or "Lise-Joelle Harrowby" is an option

pVorta.ca is my company webpage, but we are not really using the logo or company name much so it does not need to feature

Oh, and I am Canadian and an outdoor lover :-) that means that silhouettes of maple leaves, and moose and other Canadian symbols would be something I like also...*AND* I recently caught my hair and now have bangs (fringe) so if you are making an image of me that is important. Also I have green eyes. - I will upload a photo. Added Thursday, November 24, 2016

Target Market(s)

My viewers are currently majority 25-35 year old males, but am trying to appeal to girls too.

Industry/Entity Type

Computer Security

Logo Text

LJ Harrowby

Logo styles of interest
Pictorial/Combination Logo
Font styles to use
Sans Serif
Decorative
Script
Other font styles liked:
• Blackboard

Colors
33a6d7
33b8a4
00a990
3276b5
0255a3
6b449b
b7a5cd
fbee3e
faa54b

Requirements
Must have
• Must conform to the clipstream channel art template and look great on all devices: TV, computer, tablet and phone. 2560 x 1440 px and 4MB or smaller in JPEG or PNG format
• Channel templates can be found here
• https://help.quorvel.example/clipstream/answer/5810446?hl=en
• On a TV display, the whole image is displayed as channel art. The aspect ratio is 16:9 (i.e. 2560 x 1440 px).
• Minimum width: 2048 X 1152 px. This is the "safe area," where text and logos are guaranteed not to be cut off when displayed on different devices.
• Maximum width: 2560 X 423 px. This means that the "safe area" is always visible; the areas to each side of the channel art are visible depending on the viewer’s browser size.
• File size: 4MB or smaller recommended.
• If you're not sure about the width and height of an image, download our Channel Art Templates to see how images show on different devices. You can use your computer's image editor or find one online to resize the images.
Nice to have
• I'm pretty open, but here is what I like:
• - colours blue, green, bright and spring like
• - unisex appeal
• - cool girl hackers are okay
• - I like birds, stylized doves are good, hummingbirds are a favorite
• - cartoon or anime girls may appeal to me. with dreadlocks or yarn-like hair are a bonus - if you do an illustration of me, I have green eyes and bangs (fringe)
• - design should be fun but elegant
Should not have
• Here is what I don't like:
• - pictures of "hackers" - boys with hoodies on
• - pictures of circuit boards

```html
<!DOCTYPE html>
<html lang="en">
<head>
<meta charset="utf-8">
<title>LJ Harrowby – ClipStream Channel Banner</title>
<link rel="stylesheet" href="https://fonts.googleapis.com/css2?family=Oswald:wght@700&display=swap">
<style>
  :root {
    --sky-outer: #4f5c88;
    --sky-mid: #5a73a6;
    --sky-glow: #6f93c2;
    --band-deep: #12327f;
    --band-mid: #1d5aa8;
    --band-glow: #3a86bf;
    --rail-green: #10a98c;
    --rail-edge: #7fd6c4;
    --plate-teal: #139d95;
    --plate-teal-dark: #0f7f86;
    --name-yellow: #f6e845;
    --star: #dff3ff;
    --figure-area-top: rgba(150, 175, 215, 0.35);
    --figure-area-bottom: rgba(120, 150, 200, 0.2);
  }
  * { margin: 0; padding: 0; box-sizing: border-box; }
  html, body {
    width: 1200px; height: 675px; overflow: hidden;
    background: var(--sky-outer);
  }
  .banner {
    position: relative; width: 1200px; height: 675px; overflow: hidden;
    background:
      radial-gradient(ellipse 520px 300px at 600px 470px, var(--sky-glow) 0%, transparent 70%),
      linear-gradient(180deg, var(--sky-mid) 0%, var(--sky-outer) 40%, var(--sky-mid) 75%, var(--sky-outer) 100%);
  }
  .facets, .starfield { position: absolute; inset: 0; }
  .safe-band {
    position: absolute; left: 0; top: 245px; width: 1200px; height: 185px;
    background:
      radial-gradient(ellipse 330px 150px at 590px 120px, var(--band-glow) 0%, transparent 75%),
      linear-gradient(90deg, var(--band-mid) 0%, var(--band-mid) 60%, var(--band-deep) 100%);
    box-shadow: inset 0 0 30px rgba(5, 20, 70, 0.6);
  }
  .rail {
    position: absolute; left: 0; width: 1200px; height: 5px;
    background: var(--rail-green);
    box-shadow: 0 0 6px var(--rail-edge);
  }
  .rail--top { top: 240px; }
  .rail--bottom { top: 430px; }
  .rail-tab { position: absolute; }
  .rail-tab--top { left: 489px; top: 244px; }
  .rail-tab--bottom { left: 713px; top: 418px; }
  .name-plate {
    position: absolute; left: 352px; top: 288px; width: 328px; height: 72px;
    background: linear-gradient(180deg, var(--plate-teal) 0%, var(--plate-teal-dark) 100%);
  }
  .channel-name {
    position: absolute; left: 326px; top: 284px; width: 370px; height: 84px;
    display: flex; align-items: center; justify-content: center;
    white-space: nowrap;
    font-family: "Oswald", sans-serif; font-weight: 700;
    font-size: 58px; line-height: 1; letter-spacing: 0;
    text-transform: uppercase; color: var(--name-yellow);
  }
  .creator-figure {
    position: absolute; left: 760px; top: 260px; width: 110px; height: 164px;
    border-radius: 6px;
    background: linear-gradient(180deg, var(--figure-area-top) 0%, var(--figure-area-bottom) 100%);
  }
</style>
</head>
<body>
<main class="banner">
  <svg class="facets" width="1200" height="675" viewBox="0 0 1200 675" aria-hidden="true">
    <polygon points="0,0 260,0 90,240" fill="#ffffff" opacity="0.04"/>
    <polygon points="620,0 1200,0 1200,230" fill="#8fb4e0" opacity="0.10"/>
    <polygon points="860,80 1200,120 1200,240 980,240" fill="#ffffff" opacity="0.05"/>
    <polygon points="0,440 260,440 0,620" fill="#ffffff" opacity="0.05"/>
    <polygon points="420,440 780,440 600,675" fill="#8fb4e0" opacity="0.09"/>
    <polygon points="900,440 1200,480 1200,675 1000,675" fill="#ffffff" opacity="0.04"/>
    <polygon points="1060,260 1200,250 1200,420" fill="#0a2160" opacity="0.25"/>
    <polygon points="0,300 180,260 0,420" fill="#0a2160" opacity="0.2"/>
  </svg>

  <div class="safe-band"></div>

  <svg class="starfield" width="1200" height="675" viewBox="0 0 1200 675" aria-hidden="true">
    <g fill="var(--star)">
      <circle cx="343" cy="191" r="2.5"/><circle cx="759" cy="163" r="2.5"/>
      <circle cx="634" cy="209" r="2"/><circle cx="225" cy="380" r="2.5"/>
      <circle cx="540" cy="270" r="3" fill="#7fe0ff"/><circle cx="690" cy="495" r="4" fill="#7fe0ff"/>
      <circle cx="478" cy="545" r="2.5"/><circle cx="994" cy="316" r="2"/>
      <circle cx="794" cy="495" r="1.8"/><circle cx="700" cy="458" r="1.6"/>
      <circle cx="623" cy="373" r="2" fill="#7fe0ff"/><circle cx="120" cy="90" r="1.4"/>
      <circle cx="900" cy="60" r="1.4"/><circle cx="1100" cy="560" r="1.4"/>
      <circle cx="300" cy="600" r="1.4"/><circle cx="460" cy="120" r="1.2"/>
      <circle cx="1010" cy="200" r="1.2"/><circle cx="180" cy="520" r="1.2"/>
    </g>
    <g stroke="var(--star)" stroke-width="1" opacity="0.8">
      <path d="M343 181v20M333 191h20"/><path d="M759 153v20M749 163h20"/>
      <path d="M225 370v20M215 380h20"/><path d="M478 535v20M468 545h20"/>
      <path d="M994 308v16M986 316h16"/><path d="M794 487v16M786 495h16"/>
    </g>
  </svg>

  <div class="rail rail--top"></div>
  <div class="rail rail--bottom"></div>
  <svg class="rail-tab rail-tab--top" width="192" height="12" viewBox="0 0 192 12" aria-hidden="true">
    <polygon points="0,0 192,0 186,12 6,12" fill="var(--rail-green)"/>
  </svg>
  <svg class="rail-tab rail-tab--bottom" width="190" height="13" viewBox="0 0 190 13" aria-hidden="true">
    <polygon points="6,0 184,0 190,13 0,13" fill="var(--rail-green)"/>
  </svg>

  <div class="name-plate"></div>
  <h1 class="channel-name">LJ Harrowby</h1>

  <div class="creator-figure" role="img" aria-label="Cartoon illustration of the creator with bangs, glasses and green eyes, sitting cross-legged with a sticker-covered laptop"></div>
</main>
</body>
</html>
```